Book jacket for Drumlore

We need a book jacket design (hard cover front, back, spine, flaps; soft cover and eBook). for a social psychology book with the general cluelessness (being "out of it") of how people function both in their personal and social lives. This is the third book written by the author, a practicing psychiatrist, and the content centers on a single subject, people's lack of genuine emotional contact, their cluelessness with themselves and with current national and world events.

Target Market(s)

People who want to better understand the state the nation and world is in now, and what they can do about it.

Font styles to use
Serif
Sans Serif

Requirements
Must have
• Bold, eye-catching cover
Nice to have
• Like the idea of separating the title word (drum lore) to better emphasize the concept of lack of contact

```html
<!DOCTYPE html>
<html lang="en">
<head>
<meta charset="utf-8">
<title>Drumlore — Book Jacket</title>
<link rel="stylesheet" href="https://fonts.googleapis.com/css2?family=Caveat+Brush&family=Montserrat:wght@800;900&display=swap">
<style>
  :root {
    --paper: #ffffff;
    --ink: #000000;
    --accent: #f7941d;
  }
  html, body {
    margin: 0;
    padding: 0;
    width: 800px;
    height: 1200px;
    overflow: hidden;
    background: var(--paper);
  }
  .book-cover {
    display: block;
    width: 800px;
    height: 1200px;
    background: var(--paper);
  }
  .title-main {
    font-family: "Montserrat", "Arial Black", sans-serif;
    font-weight: 900;
    fill: var(--ink);
  }
  .title-script {
    font-family: "Caveat Brush", "Brush Script MT", cursive;
    fill: var(--accent);
  }
  .author-name {
    font-family: "Montserrat", "Arial", sans-serif;
    font-weight: 800;
    fill: var(--ink);
  }
</style>
</head>
<body>
  <svg class="book-cover" viewBox="0 0 800 1200" xmlns="http://www.w3.org/2000/svg" aria-labelledby="cover-title">
    <title id="cover-title">Drumlore by Harold Venic M.D.</title>
    <text class="title-main" x="73" y="409" font-size="272" textLength="660" lengthAdjust="spacingAndGlyphs">DRUM</text>
    <text class="title-script" x="104" y="510" font-size="300" textLength="530" lengthAdjust="spacingAndGlyphs">LORE</text>
    <text class="author-name" x="98" y="1172" font-size="50" textLength="622" lengthAdjust="spacingAndGlyphs">HAROLD VENIC M.D.</text>
  </svg>
</body>
</html>
```